Website for a web design agency

We are a website and marketing agency. We do website design, development, and well as Quorvel and Pinglet advertising and analytics. We ourselves need a new website for our own brand. We are working on some designs in-house with our own designers, but we also wanted to see what outside designers would come up with.
We are starting off with the homepage, and here is the breakdown of the sections:
https://docs.quorvel-sample.com/document/d/7hkW2mPqRtLxZ9vBnC4sYeJ8uDfGaTo1Ni3QwEr6KbUz/edit?usp=sharing
This doc also has many links to sites we have done, which you can take screenshots of for the portfolio section.
In terms of the "look" I am going for, I want to look high-end and very beautiful designs. I found this website that I like a lot that you can use some of the elements of, just as a starting point:
http://brindlecove-sample.com/themes/pixelbazaar/html/toverin/index.html and here is another design option they have http://brindlecove-sample.com/themes/pixelbazaar/html/toverin/index-4.html
I'm also uploading my logo. The logo matches the gold and black look from these websites, but I would be open to switching to another color scheme if needed.
This is the link to my very old website, which you can use for some of the dummy text, and a pic of myself. I will be taking more pics of myself:
https://thewindyorchardpathstudio-sample.com/
We need a homepage and a portfolio page right now, but if you are the winner, we will be hiring you to make additional pages.
Updates
More designs continue to come in even today, and I want to make sure no other designers are still submitting designs.
Target Market(s)
medium and large businesses owners, and non-profits
Number of Pages Required
1 page

```html
<!DOCTYPE html>
<html lang="en">
<head>
<meta charset="utf-8">
<title>Kestrel Strategies — Website Development and Online Marketing</title>
<link rel="stylesheet" href="https://fonts.googleapis.com/css2?family=Montserrat:ital,wght@0,400;0,500;0,600;0,700;1,400&display=swap">
<style>
:root{
  --gold:#f4b41a;
  --gold-dark:#6e5314;
  --black:#000;
  --panel:#0e0e0e;
  --card:#0b0b0b;
  --line:#2e2e2e;
  --text:#fff;
  --muted:#cfcfcf;
  --ink:#1a1a1a;
}
*{box-sizing:border-box;margin:0;padding:0}
html,body{width:1200px;height:4979px;overflow:hidden}
body{position:relative;background:var(--black);color:var(--text);font-family:'Montserrat',sans-serif}
section,header,footer{position:relative;width:1200px}
.btn{display:inline-flex;align-items:center;justify-content:center;background:var(--gold);color:var(--ink);font-size:12px;font-weight:600;text-transform:uppercase;letter-spacing:.3px}
.btn--dark{background:#2a2a2a;color:#fff}
.section-title{position:absolute;left:0;right:0;text-align:center;color:var(--gold);font-size:30px;font-weight:600;text-transform:uppercase;letter-spacing:.5px}
.section-title::after{content:"";display:block;width:44px;height:2px;background:var(--gold);margin:14px auto 0}
.dots{position:absolute;left:0;right:0;display:flex;justify-content:center;gap:6px}
.dots span{width:11px;height:11px;border-radius:50%;background:#4a4a4a}
.dots span.is-active{background:var(--gold)}

/* header */
.site-header{height:97px;background:var(--black)}
.brand{position:absolute;left:141px;top:22px;color:var(--gold);font-weight:700;line-height:1;text-transform:uppercase}
.brand__name{display:block;font-size:36px;letter-spacing:2px}
.brand__sub{display:block;font-size:16px;letter-spacing:7px;margin-top:4px}
.main-nav{position:absolute;left:491px;top:40px;display:flex;gap:32px;font-size:13px;font-weight:500;text-transform:uppercase}
.main-nav .is-active{color:var(--gold)}
.site-header .btn{position:absolute;left:918px;top:29px;width:141px;height:42px}

/* hero */
.hero{height:531px}
.hero__photo{position:absolute;inset:0;background:radial-gradient(ellipse at 72% 45%,#9a9a98 0%,#7c7c7a 40%,#5a5a58 100%)}
.hero__eyebrow{position:absolute;left:141px;top:237px;color:var(--gold);font-size:30px;font-weight:500;text-transform:uppercase}
.hero__title{position:absolute;left:141px;top:275px;font-size:39px;font-weight:500;line-height:46px;width:560px}
.hero .btn{position:absolute;left:139px;top:440px;width:184px;height:43px}

/* services */
.services{height:806px;background:var(--black)}
.services .section-title{top:77px}
.services__grid{position:absolute;left:139px;top:164px;display:grid;grid-template-columns:repeat(3,285px);column-gap:32px;row-gap:33px}
.service-card{height:261px;background:var(--card);border:1px solid var(--line);padding:0 24px;position:relative}
.service-card__icon{position:absolute;left:24px;top:31px;width:54px;height:54px;border-radius:50%;background:var(--gold);display:flex;align-items:center;justify-content:center}
.service-card__title{position:absolute;left:88px;top:31px;height:54px;display:flex;align-items:center;font-size:17px;font-weight:500;line-height:22px}
.service-card__text{position:absolute;left:24px;right:24px;top:108px;font-size:11.5px;line-height:20px;color:var(--muted)}
.service-card .btn{position:absolute;left:24px;top:195px;width:116px;height:39px;font-size:11px}

/* portfolio */
.portfolio{height:894px;background:var(--panel)}
.portfolio .section-title{top:76px}
.portfolio__grid{position:absolute;left:139px;top:166px;display:grid;grid-template-columns:repeat(3,279px);column-gap:41px;row-gap:44px}
.project-card{height:259px;background:#161616;border:1px solid var(--line);position:relative}
.project-card__shot{position:absolute;left:4px;right:4px;top:4px;height:201px}
.project-card__name{position:absolute;left:0;right:0;top:222px;text-align:center;font-size:15px;font-weight:500}
.project-card__overlay{position:absolute;left:4px;right:4px;top:4px;height:251px;background:rgba(20,20,20,.82);text-align:center;padding-top:52px}
.project-card__overlay h3{font-size:17px;font-weight:500}
.project-card__overlay p{font-size:12.5px;line-height:20px;color:var(--muted);margin:12px 22px 0}
.project-card__overlay .btn{width:116px;height:36px;margin-top:14px;font-size:11px}
.portfolio__more{position:absolute;left:502px;top:765px;width:195px;height:46px}

/* testimonials */
.testimonials{height:506px;background:var(--black)}
.testimonials .section-title{top:77px}
.testimonial__mark{position:absolute;left:559px;top:158px}
.testimonial__quote{position:absolute;left:0;right:0;top:234px;text-align:center;font-size:17.5px;font-style:italic;line-height:30px}
.testimonial__name{position:absolute;left:0;right:0;top:349px;text-align:center;font-size:17px;font-weight:500}
.testimonial__role{position:absolute;left:0;right:0;top:376px;text-align:center;font-size:13px;color:var(--gold)}
.testimonials .dots{top:409px}

/* case studies */
.cases{height:827px;background:var(--panel)}
.cases .section-title{top:79px}
.cases__grid{position:absolute;left:141px;top:166px;display:grid;grid-template-columns:repeat(2,443px);column-gap:33px}
.case-card{height:491px;background:var(--card);border-bottom:3px solid var(--gold-dark);position:relative}
.case-card__image{height:271px}
.case-card__title{position:absolute;left:33px;top:300px;font-size:18px;font-weight:500}
.case-card__text{position:absolute;left:33px;right:30px;top:332px;font-size:12px;line-height:23px;color:var(--muted)}
.case-card .btn{position:absolute;left:33px;top:422px;width:152px;height:37px;font-size:11px}
.cases__more{position:absolute;left:498px;top:700px;width:203px;height:42px}

/* team */
.team{height:914px;background:var(--black)}
.team .section-title{top:77px}
.team__grid{position:absolute;left:143px;top:168px;display:grid;grid-template-columns:repeat(4,213px);column-gap:21px}
.member{height:276px;background:var(--card);border:1px solid var(--line);position:relative}
.member__photo{height:184px;background:linear-gradient(180deg,#e9ecef 0%,#c9ced4 60%,#8d939a 100%)}
.member__badge{position:absolute;left:85px;top:162px;width:44px;height:44px;border-radius:50%;background:var(--black);display:flex;align-items:center;justify-content:center}
.member__badge i{width:32px;height:32px;border-radius:50%;background:var(--gold);display:flex;align-items:center;justify-content:center}
.member__name{position:absolute;left:0;right:0;top:218px;text-align:center;font-size:16px;font-weight:600}
.member__role{position:absolute;left:0;right:0;top:242px;text-align:center;font-size:13px;color:var(--muted)}
.team .dots{top:478px}

/* contact */
.contact{position:absolute;left:141px;top:4241px;width:918px;height:448px;background:var(--black);border:1px solid var(--line);display:flex;z-index:2}
.contact__details{width:417px;height:100%;background:var(--gold);color:var(--ink);position:relative}
.contact__title{position:absolute;left:46px;top:59px;font-size:21px;font-weight:600;text-transform:uppercase}
.contact__title::after{content:"";display:block;width:44px;height:2px;background:var(--ink);margin-top:12px}
.contact__intro{position:absolute;left:46px;right:34px;top:126px;font-size:11.5px;line-height:22px}
.contact__item{position:absolute;left:46px;display:flex;align-items:center;gap:18px;font-size:12.5px;line-height:22px}
.contact__item i{width:30px;height:30px;border-radius:50%;border:1px solid rgba(0,0,0,.35);display:flex;align-items:center;justify-content:center;flex:none}
.contact__follow{position:absolute;left:46px;top:347px;display:flex;align-items:center;gap:8px;font-size:11px;font-weight:700;text-transform:uppercase}
.contact__follow span.dot{width:27px;height:27px;border-radius:50%;background:#2b5aa8}
.contact__follow span.dot + span.dot{background:#3aa2e0}
.audit{position:relative;flex:1}
.audit__title{position:absolute;left:50px;top:59px;font-size:21px;font-weight:600;color:var(--gold);text-transform:uppercase}
.audit__title::after{content:"";display:block;width:44px;height:2px;background:var(--gold);margin-top:12px}
.field{position:absolute;font-size:12px;color:var(--muted);border-bottom:1px solid #444;height:32px}
.audit .btn{position:absolute;left:50px;top:337px;width:137px;height:44px}

/* footer */
.site-footer{height:404px;background:var(--panel)}
.site-footer .brand{left:0;right:0;top:146px;text-align:center}
.site-footer .brand__name{font-size:48px;letter-spacing:4px}
.site-footer .brand__sub{font-size:22px;letter-spacing:11px;margin-top:6px}
.footer-nav{position:absolute;left:0;right:0;top:282px;display:flex;justify-content:center;gap:34px;font-size:14px;font-weight:500;text-transform:uppercase}
.footer-nav .is-active{color:var(--gold)}
.footer-rule{position:absolute;left:141px;right:141px;top:328px;height:1px;background:var(--line)}
.copyright{position:absolute;left:0;right:0;top:364px;text-align:center;font-size:11.5px;color:var(--muted)}
</style>
</head>
<body>

<header class="site-header">
  <div class="brand"><span class="brand__name">Kestrel</span><span class="brand__sub">Strategies</span></div>
  <nav class="main-nav">
    <span class="is-active">Home</span><span>What We Do</span><span>Portfolio</span><span>Our Team</span>
  </nav>
  <a class="btn">Contact Us</a>
</header>

<section class="hero">
  <div class="hero__photo" role="img" aria-label="Photo of the agency founder speaking to camera against a grey backdrop"></div>
  <p class="hero__eyebrow">We Build Value</p>
  <h1 class="hero__title">Enterprise Level Website Development and Online Marketing</h1>
  <a class="btn">See How We Do It</a>
</section>

<section class="services">
  <h2 class="section-title">What We Do</h2>
  <div class="services__grid">
    <article class="service-card">
      <div class="service-card__icon"><svg width="28" height="28" viewBox="0 0 28 28" fill="none" stroke="#111" stroke-width="2"><rect x="4" y="5" width="20" height="15" rx="1"/><path d="M10 24h8M14 20v4M4 9h20"/></svg></div>
      <h3 class="service-card__title">Websites</h3>
      <p class="service-card__text">Lorem ipsum dolor sit a consectegtuer adipiscing elit, sed diam nonumy nibh euismod tincidunt ut laoreet.</p>
      <a class="btn">Read More</a>
    </article>
    <article class="service-card">
      <div class="service-card__icon"><svg width="28" height="28" viewBox="0 0 28 28" fill="none" stroke="#111" stroke-width="2"><rect x="5" y="4" width="18" height="20" rx="1"/><path d="M9 9h10M9 13h10M9 17h6"/></svg></div>
      <h3 class="service-card__title">Landing Pages</h3>
      <p class="service-card__text">Lorem ipsum dolor sit a consectegtuer adipiscing elit, sed diam nonumy nibh euismod tincidunt ut laoreet.</p>
      <a class="btn btn--dark">Read More</a>
    </article>
    <article class="service-card">
      <div class="service-card__icon"><svg width="28" height="28" viewBox="0 0 28 28" fill="none" stroke="#111" stroke-width="2"><rect x="4" y="6" width="20" height="16" rx="1"/><path d="M14 19c-4-3-5-4.5-5-6.2a2.4 2.4 0 0 1 5-1 2.4 2.4 0 0 1 5 1c0 1.7-1 3.2-5 6.2z"/></svg></div>
      <h3 class="service-card__title">Donation Pages</h3>
      <p class="service-card__text">Lorem ipsum dolor sit a consectegtuer adipiscing elit, sed diam nonumy nibh euismod tincidunt ut laoreet.</p>
      <a class="btn btn--dark">Read More</a>
    </article>
    <article class="service-card">
      <div class="service-card__icon"><svg width="28" height="28" viewBox="0 0 28 28" fill="none" stroke="#111" stroke-width="2"><circle cx="14" cy="14" r="10"/><path d="M17 10.5c-.8-1-2-1.5-3-1.5-1.8 0-3 1-3 2.4 0 3 6 1.8 6 4.8 0 1.4-1.3 2.4-3 2.4-1.2 0-2.4-.6-3.1-1.6M14 7.5v2M14 18.5v2"/></svg></div>
      <h3 class="service-card__title">PPC and Funnels</h3>
      <p class="service-card__text">Lorem ipsum dolor sit a consectegtuer adipiscing elit, sed diam nonumy nibh euismod tincidunt ut laoreet.</p>
      <a class="btn btn--dark">Read More</a>
    </article>
    <article class="service-card">
      <div class="service-card__icon"><svg width="28" height="28" viewBox="0 0 28 28" fill="none" stroke="#111" stroke-width="2"><rect x="4" y="7" width="20" height="15" rx="1"/><path d="M12 11.5v6l5-3z" fill="#111"/></svg></div>
      <h3 class="service-card__title">Video Marketing</h3>
      <p class="service-card__text">Lorem ipsum dolor sit a consectegtuer adipiscing elit, sed diam nonumy nibh euismod tincidunt ut laoreet.</p>
      <a class="btn btn--dark">Read More</a>
    </article>
    <article class="service-card">
      <div class="service-card__icon"><svg width="28" height="28" viewBox="0 0 28 28" fill="none" stroke="#111" stroke-width="2"><circle cx="12" cy="12" r="7"/><path d="M17 17l6 6M9 14l2-3 2 2 2-3"/></svg></div>
      <h3 class="service-card__title">Analytics &amp;<br>Optimization</h3>
      <p class="service-card__text">Lorem ipsum dolor sit a consectegtuer adipiscing elit, sed diam nonumy nibh euismod tincidunt ut laoreet.</p>
      <a class="btn btn--dark">Read More</a>
    </article>
  </div>
</section>

<section class="portfolio">
  <h2 class="section-title">Our Portfolio</h2>
  <div class="portfolio__grid">
    <article class="project-card">
      <div class="project-card__shot" role="img" aria-label="Homepage screenshot of the Tavor Productions website" style="background:linear-gradient(180deg,#fff 0 12%,#1d3c78 12% 55%,#fff 55% 78%,#6b3a2a 78%)"></div>
      <h3 class="project-card__name">Tavor Productions</h3>
    </article>
    <article class="project-card">
      <div class="project-card__shot" role="img" aria-label="Homepage screenshot of the Merin Lev Studio website" style="background:linear-gradient(180deg,#3a2a2e,#5a5a5a)"></div>
      <div class="project-card__overlay">
        <h3>Merin Lev Studio</h3>
        <p>Lorem ipsum dolor sit consectetuer adipiscing elit, sed diam nonummy nibh euismod tincidunt ut.</p>
        <a class="btn">Visit Site</a>
      </div>
    </article>
    <article class="project-card">
      <div class="project-card__shot" role="img" aria-label="Homepage screenshot of the Ostrelle construction website" style="background:linear-gradient(180deg,#fff 0 6%,#2c3a78 6% 88%,#fff 88%)"></div>
      <h3 class="project-card__name">Ostrelle</h3>
    </article>
    <article class="project-card">
      <div class="project-card__shot" role="img" aria-label="Homepage screenshot of the Velin Decor website" style="background:linear-gradient(180deg,#4a3a32 0 50%,#fff 50%)"></div>
      <h3 class="project-card__name">Velin Decor</h3>
    </article>
    <article class="project-card">
      <div class="project-card__shot" role="img" aria-label="Homepage screenshot of the Harbor Drive website" style="background:linear-gradient(180deg,#1f3d8a 0 6%,#6a86c8 6% 50%,#2a418c 50%)"></div>
      <h3 class="project-card__name">Harbor Drive</h3>
    </article>
    <article class="project-card">
      <div class="project-card__shot" role="img" aria-label="Homepage screenshot of the Nomi Arlen coaching website" style="background:linear-gradient(180deg,#f4ecea,#fff 80%,#f7e1dc)"></div>
      <h3 class="project-card__name">Nomi Arlen</h3>
    </article>
  </div>
  <a class="btn portfolio__more">View All Portfolio</a>
</section>

<section class="testimonials">
  <h2 class="section-title">Client Testimonials</h2>
  <svg class="testimonial__mark" width="82" height="60" viewBox="0 0 82 60" fill="none" stroke="#f4b41a" stroke-width="2.5"><path d="M10 6c9 0 15 6 15 15 0 16-11 30-21 35 6-8 9-14 9-20-7-1-12-6-12-14C1 13 5 6 10 6zM52 6c9 0 15 6 15 15 0 16-11 30-21 35 6-8 9-14 9-20-7-1-12-6-12-14 0-9 4-16 9-16z"/></svg>
  <p class="testimonial__quote">" Lorem ipsum dolor sit amet, consectetuer adipiscing elit, sed diam<br>nonmmy nibh euismod tincidunt ut laoreet dolore magna aliquam erat volutpat.<br>Ut wisi enim ad minim veniam, quis nostrud exerci "</p>
  <p class="testimonial__name">Daniel Corvo</p>
  <p class="testimonial__role">Ut Laoreet Dolore Aliquam Erat</p>
  <div class="dots"><span></span><span class="is-active"></span><span></span><span></span></div>
</section>

<section class="cases">
  <h2 class="section-title">Case Studies</h2>
  <div class="cases__grid">
    <article class="case-card">
      <div class="case-card__image" role="img" aria-label="Developer working at a laptop with code on a monitor" style="background:linear-gradient(135deg,#4a5d73,#1f2a38)"></div>
      <h3 class="case-card__title">Lorem ipsum dolor sit consuer.</h3>
      <p class="case-card__text">Lorem ipsum dolor sit amet, consectetuer adipiscing sed diam nonummy nibh euismod tincidunt ut laoreet dolore na aliquam erat volutpat. Ut wisi enim ad minim veniam.</p>
      <a class="btn btn--dark">View Case Studie</a>
    </article>
    <article class="case-card">
      <div class="case-card__image" role="img" aria-label="Designer working on a laptop in a café" style="background:linear-gradient(135deg,#5a7072,#2a3436)"></div>
      <h3 class="case-card__title">Lorem ipsum dolor sit consuer.</h3>
      <p class="case-card__text">Lorem ipsum dolor sit amet, consectetuer adipiscing sed diam nonummy nibh euismod tincidunt ut laoreet dolore na aliquam erat volutpat. Ut wisi enim ad minim veniam.</p>
      <a class="btn btn--dark">View Case Studie</a>
    </article>
  </div>
  <a class="btn cases__more">View All Case Studie</a>
</section>

<section class="team">
  <h2 class="section-title">Our Team</h2>
  <div class="team__grid">
    <article class="member"><div class="member__photo" role="img" aria-label="Portrait of a team member in a dark suit"></div><div class="member__badge"><i><svg width="14" height="11" viewBox="0 0 14 11" fill="#111"><path d="M0 0h14v1.2L7 6 0 1.2z"/><path d="M0 2.6l7 4.8 7-4.8V11H0z"/></svg></i></div><h3 class="member__name">JHONE DOE</h3><p class="member__role">Designation</p></article>
    <article class="member"><div class="member__photo" role="img" aria-label="Portrait of a team member in a dark blazer"></div><div class="member__badge"><i><svg width="14" height="11" viewBox="0 0 14 11" fill="#111"><path d="M0 0h14v1.2L7 6 0 1.2z"/><path d="M0 2.6l7 4.8 7-4.8V11H0z"/></svg></i></div><h3 class="member__name">JHONE DOE</h3><p class="member__role">Designation</p></article>
    <article class="member"><div class="member__photo" role="img" aria-label="Portrait of a team member in a navy suit"></div><div class="member__badge"><i><svg width="14" height="11" viewBox="0 0 14 11" fill="#111"><path d="M0 0h14v1.2L7 6 0 1.2z"/><path d="M0 2.6l7 4.8 7-4.8V11H0z"/></svg></i></div><h3 class="member__name">JHONE DOE</h3><p class="member__role">Designation</p></article>
    <article class="member"><div class="member__photo" role="img" aria-label="Portrait of a team member in a light blazer"></div><div class="member__badge"><i><svg width="14" height="11" viewBox="0 0 14 11" fill="#111"><path d="M0 0h14v1.2L7 6 0 1.2z"/><path d="M0 2.6l7 4.8 7-4.8V11H0z"/></svg></i></div><h3 class="member__name">JHONE DOE</h3><p class="member__role">Designation</p></article>
  </div>
  <div class="dots"><span></span><span class="is-active"></span><span></span><span></span></div>
</section>

<div class="contact">
  <div class="contact__details">
    <h2 class="contact__title">Contact Details</h2>
    <p class="contact__intro">Ut wisi enim ad minim veniam, quis nostrud exerci tation ullamcorper suscipit lobortis nisl ut aliquip.</p>
    <p class="contact__item" style="top:194px"><i><svg width="12" height="15" viewBox="0 0 12 15" fill="none" stroke="#1a1a1a" stroke-width="1.4"><path d="M6 14s5-5 5-8.5A5 5 0 0 0 1 5.5C1 9 6 14 6 14z"/><circle cx="6" cy="5.5" r="1.8"/></svg></i><span>123 Lorem ipsum dolor sit amet,<br>consectetuer adipiscing.</span></p>
    <p class="contact__item" style="top:252px"><i><svg width="14" height="11" viewBox="0 0 14 11" fill="none" stroke="#1a1a1a" stroke-width="1.3"><rect x=".7" y=".7" width="12.6" height="9.6"/><path d="M.7 1l6.3 5 6.3-5"/></svg></i><span>info@kestrelstrategies-sample.com</span></p>
    <p class="contact__item" style="top:298px"><i><svg width="13" height="13" viewBox="0 0 13 13" fill="none" stroke="#1a1a1a" stroke-width="1.3"><path d="M3 1l2 3-1.3 1.3a7 7 0 0 0 4 4L9 8l3 2-1 2C6 12 1 7 1 2z"/></svg></i><span>123-456-7890</span></p>
    <p class="contact__follow">Follow Us: <span class="dot"></span><span class="dot"></span></p>
  </div>
  <form class="audit">
    <h2 class="audit__title">Get a Free Audit &amp; Consultation</h2>
    <div class="field" style="left:50px;top:129px;width:193px">First Name</div>
    <div class="field" style="left:260px;top:129px;width:193px">Last Name</div>
    <div class="field" style="left:50px;top:182px;width:193px">Phone</div>
    <div class="field" style="left:260px;top:182px;width:193px">Email</div>
    <div class="field" style="left:50px;top:236px;width:403px;height:62px">Message</div>
    <a class="btn">Submit Now</a>
  </form>
</div>

<footer class="site-footer">
  <div class="brand"><span class="brand__name">Kestrel</span><span class="brand__sub">Strategies</span></div>
  <nav class="footer-nav"><span class="is-active">Home</span><span>What We Do</span><span>Portfolio</span><span>Our Team</span><span>Contact Us</span></nav>
  <div class="footer-rule"></div>
  <p class="copyright">Copyright © 2021 Kestrel Strategies. All Rights Reserved.</p>
</footer>

</body>
</html>
```